Brochure Design Project

I require a brochure with inserts inside that show our different services for different industries.

The insides of the brochure will have "about our company" ie, trackered vans - pda's and software used - images of the team and showing we invest in the very latest equipment and softwares to offer the best highest quality service. etc etc then the inserts demonstrating what we can do for each industry - images working on sites, equipment used etc etc on the back of each sheet a case study proving implementation.

Construction
Public Transport
Hotel & Leisure
Retail / Businesses
Housing Association

The inserts I imagine will be different in size or cut differently down the sides in order to allow the reader to see the different sectors and go to the one they require. The brochure will go in full to some companies - like facilities management whom would be interested in all the work we do for industries - however the brochure may contain just one of the inserts if we visit say a construction site in which they would only be interested in one (construction)

The inserts will show all the services we offer for that industry and maybe to the rear have a case study in which proves our implementation of service.

Our overall company is to offer solutions for damaged , worn or complete change of style to surfaces. For example we offer invisible damage repairs to surfaces like woods, laminates, ceramics etc.
We offer full scale resurfacing from bath re-enamelling to commercial spraying of powdercoating, metal work on offices.

also must have slot for business card.

Our communication to the customer is that using our services you can repair or resurface items back to new at the fraction of the cost of replacement thus reducing landfil as you are replacing not repairing. You get the brand new finish for a lot less cost - time and mess.

VELTAR - cutting cost with the environment in mind.

Target Market(s)

Various sectors as indicated. Business card slot.

Industry/Entity Type

Communication

Requirements
Must have
• inserts cut down the side in a way that looks good when one single insert is added but all look great showing through each sector when all added together.

```html
<!DOCTYPE html>
<html lang="en">
<head>
<meta charset="utf-8">
<title>Veltar Sector Inserts</title>
<link rel="stylesheet" href="https://fonts.googleapis.com/css2?family=Arimo:wght@400;700&display=swap">
<style>
:root{
  --backdrop:#8d8c89;
  --paper:#ffffff;
  --ink:#2f2f2f;
  --housing:#ec4f9a;
  --housing-soft:#fbe1ed;
  --transport:#f4c542;
  --transport-soft:#fdf3d6;
  --rail-red:#d7192f;
  --contact-green:#8dc63f;
  --c-blue:#29a9e0;
  --c-green:#8dc63f;
  --c-yellow:#f7d117;
  --c-orange:#f7941d;
  --c-pink:#ec1c8e;
  --c-purple:#8e4ea5;
}
*{box-sizing:border-box;margin:0;padding:0}
html,body{width:1200px;height:570px;overflow:hidden;background:var(--backdrop);font-family:"Arimo",Arial,sans-serif;color:var(--ink)}
.canvas{position:relative;width:1200px;height:570px}
.sheet{position:absolute;top:42px;width:350px;height:495px;background:var(--paper);box-shadow:0 2px 8px rgba(0,0,0,.35);overflow:hidden}
.sheet--housing{left:38px;--accent:var(--housing);--accent-soft:var(--housing-soft)}
.sheet--transport{left:425px;--accent:var(--transport);--accent-soft:var(--transport-soft)}
.sheet--case{left:810px;width:352px}
.abs{position:absolute}
.brand{left:14px;top:12px}
.brand__mark{width:26px;height:26px;border-radius:50%;background:var(--ink);margin-left:8px}
.brand__name{font-size:20px;font-weight:700;letter-spacing:.5px;margin-top:8px;line-height:1}
.slogan{left:14px;top:88px;font-size:4px;color:var(--ink)}
.ribbon{top:0;right:0;width:120px;height:120px}
.sector-band{left:0;top:118px;width:100%;height:18px;background:var(--accent-soft)}
.sector-band__title{position:absolute;left:20px;top:4px;font-size:9px;color:var(--accent)}
.body-heading{left:18px;top:143px;font-size:7.5px}
.body-copy{font-size:5.4px;line-height:7.5px;color:#444}
.body-copy p{text-indent:6px}
.col-a{left:18px;top:153px;width:150px}
.col-b{left:180px;top:142px;width:152px}
.feature-strip{left:0;top:362px;width:100%;height:14px;background:var(--accent-soft)}
.feature{top:333px}
.feature__img{height:45px}
.feature__cap{height:24px;background:var(--accent-soft);font-size:5.2px;color:#b5b5b5;padding:3px 2px;line-height:6.5px}
.img-van{background:linear-gradient(160deg,#b9b3ad,#6c5f58 55%,#a82c2c)}
.img-pda{background:linear-gradient(150deg,#dfe3e6,#c9a88a 60%,#e4e7ea)}
.img-soft{background:linear-gradient(120deg,#27306e,#6076b8 50%,#9aa3d0)}
.img-team{background:linear-gradient(140deg,#b8c5cc,#e0c79e 45%,#4a7fa8)}
.company{left:262px;top:422px;font-size:5.2px;line-height:6.6px}
.company__name{font-weight:700;margin-bottom:7px}
.company__contact{margin-top:8px}
.company__contact b{color:var(--contact-green);display:inline-block;width:8px}
.badges{left:14px;top:463px;display:flex;gap:4px}
.badge{width:20px;height:15px;background:#d3d6dc;border-radius:2px}
.badge--round{border-radius:50%;width:16px}
.rail-name{right:18px;top:36px;font-size:11px;font-weight:700;color:var(--rail-red)}
.case-photo{left:0;top:115px;width:100%;height:270px;background:radial-gradient(ellipse at 40% 65%,#b34a4a 0%,#7d2c33 22%,transparent 45%),linear-gradient(180deg,#2b2f33,#5c5955 55%,#8a6c3a)}
.case-bar{left:0;top:115px;width:100%;height:18px;background:rgba(40,40,40,.55);color:#fff;font-size:8.5px;padding:4px 20px}
.case-panel{left:175px;top:140px;width:160px;height:190px;background:rgba(255,255,255,.72);padding:6px 7px}
.case-panel h3{font-size:7px;font-weight:400;margin-bottom:2px}
.case-thumb{top:387px;height:43px}
.thumb-worker{background:linear-gradient(150deg,#8b6b4d,#d7c94b 55%,#4d4239)}
.thumb-window{background:linear-gradient(180deg,#d5d2cc,#7f7a72)}
.thumb-cabin{background:linear-gradient(160deg,#c8ccd0,#8c8a86)}
.case-note{left:180px;top:390px;width:152px}
</style>
</head>
<body>
<div class="canvas">

  <section class="sheet sheet--housing">
    <div class="abs brand">
      <div class="brand__mark"></div>
      <div class="brand__name">VELTAR</div>
    </div>
    <div class="abs slogan">VELTAR - cutting cost with the environment in mind.</div>
    <svg class="abs ribbon" viewBox="0 0 120 120" font-family="Arimo, Arial, sans-serif" font-size="5.5" fill="#fff">
      <polygon points="0,0 12,0 120,108 120,120" fill="var(--c-purple)"/>
      <polygon points="12,0 24,0 120,96 120,108" fill="var(--c-pink)"/>
      <polygon points="24,0 36,0 120,84 120,96" fill="var(--c-orange)"/>
      <polygon points="36,0 48,0 120,72 120,84" fill="var(--c-yellow)"/>
      <polygon points="48,0 60,0 120,60 120,72" fill="var(--c-green)"/>
      <polygon points="60,0 72,0 120,48 120,60" fill="var(--c-blue)"/>
      <text transform="translate(69.2,6) rotate(45)">Construction</text>
      <text transform="translate(57.2,6) rotate(45)">Hotel &amp; Leisure</text>
      <text transform="translate(45.2,6) rotate(45)">Education Sector</text>
      <text transform="translate(33.2,6) rotate(45)">Public Transport</text>
      <text transform="translate(21.2,6) rotate(45)">Retail / Businesses</text>
      <text transform="translate(9.2,6) rotate(45)">Housing Association</text>
    </svg>
    <div class="abs sector-band"><span class="sector-band__title">Housing Association</span></div>
    <h2 class="abs body-heading">Main Heading</h2>
    <div class="abs body-copy col-a">
      <p>Lorem ipsum dolor sit amet, consectetuer a scing elit. Aenean commodo ligula eget doenean massa entesque tesque eused.</p>
      <p>Cum sis natoque penatibus et magnis dis partient use montes, nascetur ridiculus mus. Donec quamsed felised, ultricies nec, pellentesque eu, pretium quesm. Nullaterds consequat massa quis enimpartient montes, nascetured ridiculus mus.</p>
      <p>Donec pede justo, fringilla velade, alique vulputed eget, arcu. In enim justo rhoncus utterd imperdieta, venensed atis vitae, justo. Nullam dictum felis euered pedelleds at mollad pretium integer tincidunt.</p>
      <p>Lorem ipsum dolor sit amet, consectetuer andds trade adipiscing elit. Aenean commodo ligula eget dolor. Cum sociis natoque penatibus et magnis disereds dictum felis partur montes, nascetur ridiculus mus. Donec quam felis,</p>
    </div>
    <div class="abs body-copy col-b">
      <p>ultricies nec, pellentesque eu, pretium quised, sem. Nulla consequat massa quis enim.</p>
      <p>Donec pede justo, fringilla vel, aliquet neckerseds and, vulputate eget, arcu. In enim justo, rhoncus uttered, use imperdiet a, venenatis vitae, justo. Nullam dictums felise eu pede mollis pretium. Integer tincidunt. Cras dapib us. Vivamus elementum semper nisi. Aenean vulputate.</p>
      <p>Lorem ipsum dolor sit amet, consectetuer adipiplering scing elit. Aenean commodo ligula eget doenean massa entesque.</p>
      <p>Cum sis natoque penatibus et magnis dis partient atte montes, nascetur ridiculus mus. Donec quamsed felis, ultricies nec, pellentesque eupartient montes, nascetur ridiculus arcu. In enim justo, rhoncus uttered, imperdiet a, venenatis vitae, justo. Nullam dictums felis eu pede mollis pretium. Integer tincidunt. Cras dapibus.</p>
    </div>
    <div class="abs feature-strip"></div>
    <div class="abs feature" style="left:14px;width:46px"><div class="feature__img img-van" role="img" aria-label="Company van parked outside"></div><div class="feature__cap">trackered vans.</div></div>
    <div class="abs feature" style="left:66px;width:46px"><div class="feature__img img-pda" role="img" aria-label="Engineer using a handheld PDA"></div><div class="feature__cap">pda's.</div></div>
    <div class="abs feature" style="left:117px;width:97px"><div class="feature__img img-soft" role="img" aria-label="Software on a digital screen"></div><div class="feature__cap">softwares that offer the best highest quality service.</div></div>
    <div class="abs feature" style="left:220px;width:97px"><div class="feature__img img-team" role="img" aria-label="Team reviewing plans on site"></div><div class="feature__cap">softwares that offer the best highest quality service.</div></div>
    <div class="abs company">
      <div class="company__name">Veltar Surface Solutions Ltd</div>
      <div>Unit 4, Larkfield Court<br>Northgate Business Park<br>Stockport, SK9 2QT</div>
      <div class="company__contact"><b>T</b>0161 555 0148<br><b>E</b>info@veltar.co.uk<br><b>W</b>www.veltar.co.uk</div>
    </div>
    <div class="abs badges"><div class="badge"></div><div class="badge"></div><div class="badge badge--round"></div></div>
  </section>

  <section class="sheet sheet--transport">
    <div class="abs brand">
      <div class="brand__mark"></div>
      <div class="brand__name">VELTAR</div>
    </div>
    <div class="abs slogan">VELTAR - cutting cost with the environment in mind.</div>
    <svg class="abs ribbon" viewBox="0 0 120 120" font-family="Arimo, Arial, sans-serif" font-size="5.5" fill="#fff">
      <polygon points="60,0 72,0 120,48 120,60" fill="var(--transport)"/>
      <text transform="translate(69.2,6) rotate(45)">Public Transport</text>
    </svg>
    <div class="abs sector-band"><span class="sector-band__title">Public Trasport</span></div>
    <h2 class="abs body-heading">Main Heading</h2>
    <div class="abs body-copy col-a">
      <p>Lorem ipsum dolor sit amet, consectetuer a scing elit. Aenean commodo ligula eget doenean massa entesque tesque eused.</p>
      <p>Cum sis natoque penatibus et magnis dis partient use montes, nascetur ridiculus mus. Donec quamsed felised, ultricies nec, pellentesque eu, pretium quesm. Nullaterds consequat massa quis enimpartient montes, nascetured ridiculus mus.</p>
      <p>Donec pede justo, fringilla velade, alique vulputed eget, arcu. In enim justo rhoncus utterd imperdieta, venensed atis vitae, justo. Nullam dictum felis euered pedelleds at mollad pretium integer tincidunt.</p>
      <p>Lorem ipsum dolor sit amet, consectetuer andds trade adipiscing elit. Aenean commodo ligula eget dolor. Cum sociis natoque penatibus et magnis disereds dictum felis partur montes, nascetur ridiculus mus. Donec quam felis,</p>
    </div>
    <div class="abs body-copy col-b">
      <p>ultricies nec, pellentesque eu, pretium quised, sem. Nulla consequat massa quis enim.</p>
      <p>Donec pede justo, fringilla vel, aliquet neckerseds and, vulputate eget, arcu. In enim justo, rhoncus uttered, use imperdiet a, venenatis vitae, justo. Nullam dictums felise eu pede mollis pretium. Integer tincidunt. Cras dapib us. Vivamus elementum semper nisi. Aenean vulputate.</p>
      <p>Lorem ipsum dolor sit amet, consectetuer adipiplering scing elit. Aenean commodo ligula eget doenean massa entesque.</p>
      <p>Cum sis natoque penatibus et magnis dis partient atte montes, nascetur ridiculus mus. Donec quamsed felis, ultricies nec, pellentesque eupartient montes, nascetur ridiculus arcu. In enim justo, rhoncus uttered, imperdiet a, venenatis vitae, justo. Nullam dictums felis eu pede mollis pretium. Integer tincidunt. Cras dapibus.</p>
    </div>
    <div class="abs feature" style="left:14px;width:46px"><div class="feature__img img-van" role="img" aria-label="Company van parked outside"></div><div class="feature__cap">trackered vans.</div></div>
    <div class="abs feature" style="left:66px;width:46px"><div class="feature__img img-pda" role="img" aria-label="Engineer using a handheld PDA"></div><div class="feature__cap">pda's.</div></div>
    <div class="abs feature" style="left:117px;width:97px"><div class="feature__img img-soft" role="img" aria-label="Software on a digital screen"></div><div class="feature__cap">softwares that offer the best highest quality service.</div></div>
    <div class="abs feature" style="left:220px;width:97px"><div class="feature__img img-team" role="img" aria-label="Team reviewing plans on site"></div><div class="feature__cap">softwares that offer the best highest quality service.</div></div>
    <div class="abs company">
      <div class="company__name">Veltar Surface Solutions Ltd</div>
      <div>Unit 4, Larkfield Court<br>Northgate Business Park<br>Stockport, SK9 2QT</div>
      <div class="company__contact"><b>T</b>0161 555 0148<br><b>E</b>info@veltar.co.uk<br><b>W</b>www.veltar.co.uk</div>
    </div>
    <div class="abs badges"><div class="badge"></div><div class="badge"></div><div class="badge badge--round"></div></div>
  </section>

  <section class="sheet sheet--case">
    <svg class="abs" style="left:0;top:0" width="80" height="80" viewBox="0 0 80 80" font-family="Arimo, Arial, sans-serif" font-size="5.5" fill="#fff">
      <polygon points="50,0 64,0 0,64 0,50" fill="var(--transport)"/>
      <text transform="translate(4,55.8) rotate(-45)">Public Transport</text>
    </svg>
    <div class="abs rail-name">Northline Rail Group</div>
    <div class="abs case-photo" role="img" aria-label="Red passenger train in a maintenance depot"></div>
    <div class="abs case-bar">Case Study Proving Implementation</div>
    <div class="abs case-panel body-copy">
      <h3>Main Heading</h3>
      <p>Lorem ipsum dolor sit amet, consectetuer a scing elit. Aenean commodo ligula eget doenean massa entesque tesque eused.</p>
      <p>Cum sis natoque penatibus et magnis dis partient use montes, nascetur ridiculus mus. Donec quamsed felis, ultricies nec, pellentesque eu, pretium quesm. Nullaterds consequat massa quis enimpartient montes, nascetur ridiculus.</p>
      <p>Donec pede justo, fringilla velade, alique vulputed eget, arcu. In enim justo rhoncus utterd imperdieta, venense atis vitae, justo. Nullam dictum felis euered pedelleds mollad pretium integer tincidunt.</p>
      <p>Lorem ipsum dolor sit amet, consectetuer andds adipiscing elit. Aenean commodo ligula eget dolor. Cum sociis natoque penatibus et magnis diseredts partur montes, nascetur ridiculus mus. Donec quam felis, ultricies nec, pellentesque eu, pretium quised, sem. Nulla consequat massa quis enim.</p>
    </div>
    <div class="abs case-thumb thumb-worker" style="left:20px;width:44px" role="img" aria-label="Technician at work on site"></div>
    <div class="abs case-thumb thumb-window" style="left:70px;width:44px" role="img" aria-label="Resurfaced window frames"></div>
    <div class="abs case-thumb thumb-cabin" style="left:120px;width:46px" role="img" aria-label="Refinished station cabin"></div>
    <div class="abs body-copy case-note">
      <p>Lorem ipsum dolor sit amet, consectetuer a scing elit. Aenean commodo ligula eget doenean massa entesque tesque eused. Cum sis natoque penatibus et magnis dis partient montes, nascetur ridiculus mus. Donec quamsed felis, ultricies nec, pellentesque eu, pretium quesm. Nulla consequat massa quis enimpartient montes, nascetur ridiculus mus.</p>
    </div>
  </section>

</div>
</body>
</html>
```